New Business Card Design Project

The legal name of the company is TTTolvane, we also refer to it as simply Tolvane or you could also use the initials TTT...... please feel creative.
Excellent design.
On the second side, if you could image North and South America on each drop of water ... it almost looks like that now.
The website is www.tttolvane.com
Attached is another card with the required information; no addresses.

Industry/Entity Type

Legal

```html
<!DOCTYPE html>
<html lang="en">
<head>
<meta charset="utf-8">
<title>Tolvane Business Card</title>
<link rel="stylesheet" href="https://fonts.googleapis.com/css2?family=Nunito:wght@300;400;700;800&display=swap">
<style>
  :root {
    --canvas: #ffffff;
    --card: #3a3a3c;
    --ink: #ffffff;
    --rule: #ffffff;
    --globe-deep: #2f4f9c;
    --globe-mid: #5a79bf;
    --globe-light: #eef2fb;
  }
  * { margin: 0; padding: 0; box-sizing: border-box; }
  html, body { width: 1200px; height: 1000px; overflow: hidden; background: var(--canvas); }
  body { position: relative; font-family: "Nunito", sans-serif; color: var(--ink); }

  .card { position: absolute; top: 153px; width: 328px; height: 574px; background: var(--card); overflow: hidden; }
  .card-front { left: 265px; }
  .card-back { left: 613px; width: 327px; }

  .rule-vertical { position: absolute; left: 40px; top: 0; width: 2px; height: 100%; background: var(--rule); }
  .rule-horizontal { position: absolute; left: 0; top: 532px; width: 100%; height: 2px; background: var(--rule); }

  .front-text { position: absolute; right: 34px; text-align: right; white-space: nowrap; }
  .brand-name { top: 34px; font-size: 52px; font-weight: 300; letter-spacing: 1px; line-height: 1; }
  .legal-name { top: 98px; font-size: 21px; font-weight: 300; }
  .office-label { font-size: 20px; font-weight: 800; line-height: 1.2; }
  .office-phone { font-size: 21px; font-weight: 300; line-height: 1.2; margin-bottom: 10px; }
  .offices { top: 180px; }
  .person { top: 370px; }
  .person-name { font-size: 22px; font-weight: 800; line-height: 1.3; }
  .person-title { font-size: 23px; font-weight: 300; line-height: 1.3; }
  .email { top: 458px; font-size: 20px; font-weight: 300; }
  .email strong { font-weight: 800; }

  .globe { position: absolute; left: 0; top: 0; }
  .back-footer { position: absolute; left: 0; top: 520px; width: 100%; height: 28px; }
  .back-footer .line { position: absolute; top: 13px; height: 2px; background: var(--rule); }
  .back-footer .line-left { left: 0; width: 120px; }
  .back-footer .line-right { left: 292px; width: 35px; }
  .website { position: absolute; left: 129px; top: 0; font-size: 22px; font-weight: 800; line-height: 1.2; }

  .footer-band { position: absolute; left: 0; top: 880px; width: 1200px; height: 120px; background: var(--card); }
  .footer-brand { position: absolute; right: 42px; top: 24px; font-size: 64px; font-weight: 300; letter-spacing: 1px; line-height: 1; }
</style>
</head>
<body>
  <section class="card card-front">
    <div class="rule-vertical"></div>
    <div class="rule-horizontal"></div>
    <h1 class="front-text brand-name">TOLVANE</h1>
    <p class="front-text legal-name">tttolvane sa, llc</p>
    <div class="front-text offices">
      <p class="office-label">Guatemala</p>
      <p class="office-phone">+502 5871 4320</p>
      <p class="office-label">USA</p>
      <p class="office-phone">+1 305 555 0148</p>
    </div>
    <div class="front-text person">
      <p class="person-name">DAX ORLEN</p>
      <p class="person-title">Managing Director</p>
    </div>
    <p class="front-text email">dao@<strong>tolvane.com</strong></p>
  </section>

  <section class="card card-back">
    <svg class="globe" width="327" height="500" viewBox="0 0 327 500" role="img" aria-label="Globe showing North and South America">
      <defs>
        <radialGradient id="globeShade" cx="0.62" cy="0.58" r="0.65">
          <stop offset="0" stop-color="var(--globe-light)"/>
          <stop offset="0.45" stop-color="var(--globe-mid)"/>
          <stop offset="1" stop-color="var(--globe-deep)"/>
        </radialGradient>
      </defs>
      <circle cx="178" cy="232" r="246" fill="url(#globeShade)"/>
    </svg>
    <div class="back-footer">
      <span class="line line-left"></span>
      <span class="website">tolvane.com</span>
      <span class="line line-right"></span>
    </div>
  </section>

  <footer class="footer-band">
    <p class="footer-brand">TOLVANE</p>
  </footer>
</body>
</html>
```